HarborRise Summer Brunch

This flyer is designed to market the upcoming conference in July

Target Market(s)

African American Christian Men and Women

Font styles to use
Decorative

Requirements
Must have
• This flyer is to represent both men and women as follows:
• Although offered on the same day and same location - Men and Women must appear two meetings in one location
• 1. BOS - Brothers of Steel
• 2. GRVW - Grounded and Rooted in Virtue and Worth - Women
• Theme: "2020 - Walking With Courage" (Ephesians 6:10-15)
• Date: June 27, 2020
Nice to have
• *Distinct between the two meetings in one
• * Unified brand coupled with Men and Women targets
• * Vibrant, energized, active flyer to communicate promise and hope
Should not have
• Profanity, clip art, etc.

```html
<!DOCTYPE html>
<html lang="en">
<head>
<meta charset="utf-8">
<title>HarborRise Flyer Design</title>
<link href="https://fonts.googleapis.com/css2?family=Abril+Fatface&family=Montserrat:ital,wght@0,700;1,400&family=Oswald:wght@400&family=Roboto:wght@400&display=swap" rel="stylesheet">
<style>
  :root {
    --board: #8c8c8c;
    --board-title: #e9e9e9;
    --ink: #0a0a0a;
    --white: #ffffff;
    --gold-dark: #8a6414;
    --gold: #c8961e;
    --gold-light: #f3d77a;
    --text-dark: #1a1a1a;
    --gold-grad: linear-gradient(180deg, #f0cf6a 0%, #c28f1c 55%, #8a6414 100%);
    --band-grad: linear-gradient(90deg, #b9861d 0%, #f6e08a 30%, #c99522 55%, #f3d77a 80%, #a9791a 100%);
  }
  * { box-sizing: border-box; margin: 0; padding: 0; }
  html, body { width: 1200px; height: 920px; overflow: hidden; }
  body { background: var(--board); position: relative; font-family: "Oswald", sans-serif; }

  .board-title { position: absolute; left: 47px; top: 30px; display: flex; align-items: baseline; gap: 14px; }
  .board-title__main { font-family: "Montserrat", sans-serif; font-weight: 700; font-size: 56px; color: var(--board-title); letter-spacing: 1px; }
  .board-title__sub { font-family: "Montserrat", sans-serif; font-style: italic; font-weight: 400; font-size: 26px; color: var(--board-title); }

  .flyer { position: absolute; top: 115px; width: 536px; height: 757px; background: var(--ink); box-shadow: 0 4px 10px rgba(0,0,0,.35); overflow: hidden; }
  .flyer--ring { left: 45px; }
  .flyer--hex { left: 621px; }

  .flyer__band { position: absolute; left: 0; width: 100%; height: 22px; background: var(--band-grad); }
  .flyer__band--top { top: 0; }
  .flyer__band--bottom { bottom: 0; }

  .flyer__texture { position: absolute; }
  .flyer--ring .flyer__texture { left: 38px; top: 150px; width: 460px; height: 480px; border-radius: 50%;
    background: radial-gradient(ellipse at center, rgba(150,120,60,.45) 0%, rgba(90,70,35,.25) 45%, rgba(0,0,0,0) 72%); }
  .flyer--hex .flyer__texture { left: 40px; top: 110px; width: 456px; height: 600px; border-radius: 50%;
    background: radial-gradient(ellipse at center, rgba(230,180,60,.75) 0%, rgba(180,130,30,.45) 40%, rgba(0,0,0,0) 70%); }

  .meeting { position: absolute; color: var(--gold); font-family: "Abril Fatface", serif; line-height: 1; }
  .meeting__name { display: block; font-size: 64px; letter-spacing: -1px; }
  .meeting__tag { display: block; font-size: 14px; margin-top: -4px; }
  .flyer--ring .meeting--men { left: 62px; top: 74px; }
  .flyer--ring .meeting--women { right: 60px; top: 74px; text-align: right; }
  .flyer--ring .meeting--women .meeting__tag { font-size: 11px; }
  .flyer--hex .meeting__name { font-size: 52px; }
  .flyer--hex .meeting__tag { font-size: 12px; }
  .flyer--hex .meeting--men { left: 30px; top: 48px; }
  .flyer--hex .meeting--women { right: 22px; top: 48px; text-align: right; }
  .flyer--hex .meeting--women .meeting__tag { font-size: 10px; }

  .emblem { position: absolute; left: 0; top: 0; }

  .date-badge { position: absolute; text-align: center; color: var(--text-dark); font-family: "Oswald", sans-serif; line-height: 1; }
  .date-badge__day { display: block; font-size: 24px; }
  .date-badge__year { display: block; font-size: 36px; }
  .flyer--ring .date-badge { left: 210px; top: 226px; width: 110px; }
  .flyer--hex .date-badge { left: 221px; top: 218px; width: 94px; }
  .flyer--hex .date-badge__day { font-size: 20px; }
  .flyer--hex .date-badge__year { font-size: 31px; }

  .theme { position: absolute; left: 0; width: 100%; text-align: center; }
  .theme__year { display: block; font-family: "Abril Fatface", serif; font-size: 78px; line-height: 1;
    background: var(--gold-grad); -webkit-background-clip: text; background-clip: text; color: transparent; }
  .theme__title { display: block; font-size: 26px; color: var(--gold); line-height: 1.1; margin-top: 4px; }
  .theme__verse { display: block; font-family: "Roboto", sans-serif; font-size: 16px; color: var(--text-dark); margin-top: 6px; }
  .theme__time { display: block; font-size: 32px; color: var(--gold); margin-top: 4px; }
  .flyer--ring .theme { top: 325px; }
  .flyer--hex .theme { top: 314px; }
  .flyer--hex .theme__year { font-size: 76px; }
  .flyer--hex .theme__title { font-size: 25px; }

  .host { position: absolute; left: 176px; width: 184px; height: 50px; border-radius: 8px 8px 0 0;
    background: linear-gradient(180deg, #ffffff 0%, #f5ecc8 60%, #d9bb62 100%); text-align: center; padding-top: 6px; }
  .flyer--ring .host { top: 683px; }
  .flyer--hex .host { top: 677px; }
  .host__name { display: block; font-family: "Oswald", sans-serif; font-size: 22px; color: var(--text-dark); line-height: 1; }
  .host__line { display: block; font-family: "Roboto", sans-serif; font-size: 6.5px; color: var(--text-dark); letter-spacing: .3px; margin-top: 5px; }
</style>
</head>
<body>
  <header class="board-title">
    <span class="board-title__main">PREVIEW</span>
    <span class="board-title__sub">Flyer Design</span>
  </header>

  <svg width="0" height="0" style="position:absolute">
    <defs>
      <linearGradient id="gold-stroke" x1="0" y1="0" x2="1" y2="1">
        <stop offset="0" stop-color="#f6e08a"/>
        <stop offset=".45" stop-color="#b8861c"/>
        <stop offset=".7" stop-color="#f3d77a"/>
        <stop offset="1" stop-color="#8a6414"/>
      </linearGradient>
      <radialGradient id="gold-disc" cx=".4" cy=".35" r=".75">
        <stop offset="0" stop-color="#f8e08a"/>
        <stop offset=".6" stop-color="#d4a33a"/>
        <stop offset="1" stop-color="#a3761a"/>
      </radialGradient>
      <radialGradient id="inner-white" cx=".5" cy=".5" r=".5">
        <stop offset=".8" stop-color="#ffffff"/>
        <stop offset="1" stop-color="#d9d9d9"/>
      </radialGradient>
    </defs>
  </svg>

  <!-- Flyer: ring version -->
  <section class="flyer flyer--ring">
    <div class="flyer__band flyer__band--top"></div>
    <div class="flyer__texture" role="img" aria-label="Fine gold glitter dust scattered around the central emblem"></div>

    <div class="meeting meeting--men"><span class="meeting__name">BOS</span><span class="meeting__tag">Brothers of Steel</span></div>
    <div class="meeting meeting--women"><span class="meeting__name">GRVW</span><span class="meeting__tag">Grounded and Rooted in Virtue and Worth</span></div>

    <svg class="emblem" width="536" height="757" viewBox="0 0 536 757">
      <circle cx="265" cy="389" r="145" fill="none" stroke="url(#gold-stroke)" stroke-width="14"/>
      <circle cx="265" cy="389" r="134" fill="none" stroke="#6b4e12" stroke-width="4"/>
      <circle cx="265" cy="389" r="130" fill="url(#inner-white)"/>
      <circle cx="265" cy="258" r="58" fill="url(#gold-disc)" stroke="#8a6414" stroke-width="2"/>
    </svg>

    <div class="date-badge"><span class="date-badge__day">June 27</span><span class="date-badge__year">2020</span></div>

    <div class="theme">
      <span class="theme__year">2020</span>
      <span class="theme__title">Walking With Courage</span>
      <span class="theme__verse">Ephesians 6:10-15</span>
      <span class="theme__time">10am</span>
    </div>

    <div class="host"><span class="host__name">HarborRise</span><span class="host__line">LIFTING HEARTS, BUILDING STRONG NEIGHBORS</span></div>
    <div class="flyer__band flyer__band--bottom"></div>
  </section>

  <!-- Flyer: hexagon version -->
  <section class="flyer flyer--hex">
    <div class="flyer__band flyer__band--top"></div>
    <div class="flyer__texture" role="img" aria-label="Gold halftone dot pattern radiating from the centre"></div>

    <div class="meeting meeting--men"><span class="meeting__name">BOS</span><span class="meeting__tag">Brothers of Steel</span></div>
    <div class="meeting meeting--women"><span class="meeting__name">GRVW</span><span class="meeting__tag">Grounded and Rooted in Virtue and Worth</span></div>

    <svg class="emblem" width="536" height="757" viewBox="0 0 536 757">
      <polygon points="268,262 392,328 392,460 268,526 144,460 144,328" fill="#ffffff" stroke="url(#gold-stroke)" stroke-width="3"/>
      <circle cx="268" cy="247" r="48" fill="url(#gold-disc)" stroke="#8a6414" stroke-width="2"/>
    </svg>

    <div class="date-badge"><span class="date-badge__day">June 27</span><span class="date-badge__year">2020</span></div>

    <div class="theme">
      <span class="theme__year">2020</span>
      <span class="theme__title">Walking With Courage</span>
      <span class="theme__verse">Ephesians 6:10-15</span>
      <span class="theme__time">10am</span>
    </div>

    <div class="host"><span class="host__name">HarborRise</span><span class="host__line">LIFTING HEARTS, BUILDING STRONG NEIGHBORS</span></div>
    <div class="flyer__band flyer__band--bottom"></div>
  </section>
</body>
</html>
```